Brightvolt Electrical Services Needs A Flyer Design

We need a flyer design for a new business based in Sydney, Australia called Brightvolt Electrical Services. We provide services for residential,commercial and industrial works. Services include Electrical Design, Installation, Repairs & Maintenance. Communications Installation, Cabling, Maintenance & Repairs. Over 25 years Industry Experience.Service Calls, Quick Response Time, Professional Service. We would like to see designs that use the colors red,white and blue similar to the logo. The final Design should be creative as the business logo suggests and should communicate the businesses services.

Target Market(s)

Residential

Industry/Entity Type

Industrial

Font styles to use
Sans Serif

Requirements
Must have
• My project must have the logo provided utilized in the flyer.It must list the following contact name and number Ray 0491 627 318 services as above in the project description. Flyer should be DL size (99mmx210mm).

```html
<!DOCTYPE html>
<html lang="en">
<head>
<meta charset="utf-8">
<title>Brightvolt Electrical Services – DL Flyer</title>
<link rel="stylesheet" href="https://fonts.googleapis.com/css2?family=Jura:wght@400;600;700&family=Open+Sans:wght@400&display=swap">
<style>
  :root {
    --navy: #1c2553;
    --band-blue: #283a80;
    --red: #d0282c;
    --paper: #ffffff;
    --paper-grey: #f1f1f1;
    --ink: #2b2b2b;
    --band-text: #e9ecf6;
    --backdrop: #e4e4e2;
  }
  * { box-sizing: border-box; margin: 0; padding: 0; }
  html, body { width: 1200px; height: 1078px; overflow: hidden; }
  body { background: var(--backdrop); font-family: "Open Sans", sans-serif; color: var(--ink); position: relative; }

  .flyer { position: absolute; width: 931px; height: 443px; background: var(--paper); box-shadow: 0 6px 16px rgba(0,0,0,.25); overflow: hidden; }
  .flyer--front { left: 110px; top: 74px; }
  .flyer--back { left: 182px; top: 559px; }

  .brand { position: absolute; left: 43px; top: 44px; color: var(--navy); font-family: "Jura", sans-serif; font-weight: 700; line-height: 1; }
  .brand__name { display: block; font-size: 54px; letter-spacing: 4px; text-transform: uppercase; }
  .brand__sub { display: block; font-size: 16px; letter-spacing: 3px; text-transform: uppercase; margin-top: 6px; padding-left: 40px; }

  .contact { position: absolute; right: 40px; top: 88px; display: flex; align-items: center; gap: 10px; font-family: "Jura", sans-serif; font-weight: 600; font-size: 28px; letter-spacing: 4px; color: var(--ink); }
  .contact svg { width: 30px; height: 30px; }
  .contact__name { font-variant: small-caps; }

  .flyer--front .head { position: absolute; left: 0; top: 0; width: 100%; height: 138px; background: var(--paper-grey); }
  .photo-strip { position: absolute; left: 0; top: 146px; width: 100%; height: 188px; display: flex; }
  .photo { flex: 1; height: 100%; }
  .photo--plans { background: linear-gradient(135deg, #eef0f2, #d8dade 60%, #e8793a); }
  .photo--board { background: linear-gradient(135deg, #d9b9a0, #5c85b8 55%, #8a8f96); }
  .photo--stripper { background: linear-gradient(135deg, #d99a78, #c46a45 50%, #e6c9a2); }
  .photo--meter { background: linear-gradient(135deg, #40464e, #f0b91e 50%, #d6d8db); }

  .band { position: absolute; left: 0; width: 100%; background: var(--band-blue); color: var(--band-text); display: flex; align-items: center; }
  .flyer--front .band { top: 344px; height: 99px; padding-left: 48px; }
  .chevrons { width: 36px; height: 34px; }
  .band__title { font-family: "Jura", sans-serif; font-weight: 600; font-size: 26px; letter-spacing: 6px; font-variant: small-caps; margin-left: 24px; }
  .sectors { margin-left: 58px; font-size: 20px; letter-spacing: .5px; display: flex; gap: 12px; }

  .flyer--back .head { position: absolute; left: 0; top: 0; width: 100%; height: 141px; background: var(--paper); }
  .flyer--back .brand { top: 30px; }
  .flyer--back .contact { top: 89px; right: 38px; }
  .services { position: absolute; left: 0; top: 141px; width: 100%; height: 217px; background: var(--paper-grey); }
  .experience { position: absolute; right: 47px; top: 8px; font-size: 13px; letter-spacing: .5px; }
  .services__title { position: absolute; left: 54px; top: 26px; display: flex; align-items: center; gap: 18px; color: var(--red); font-family: "Jura", sans-serif; font-weight: 600; font-size: 30px; letter-spacing: 6px; font-variant: small-caps; }
  .service-list { position: absolute; top: 88px; list-style: none; font-size: 20px; letter-spacing: .5px; line-height: 35px; }
  .service-list li::before { content: "»"; margin-right: 12px; }
  .service-list--left { left: 123px; }
  .service-list--right { left: 513px; }
  .flyer--back .band { top: 366px; height: 77px; justify-content: center; font-size: 23px; letter-spacing: .6px; gap: 16px; }
</style>
</head>
<body>

<section class="flyer flyer--front">
  <header class="head">
    <div class="brand"><span class="brand__name">Brightvolt</span><span class="brand__sub">Electrical Services</span></div>
    <div class="contact">
      <svg viewBox="0 0 30 30" aria-hidden="true"><circle cx="15" cy="15" r="13" fill="none" stroke="#2b2b2b" stroke-width="2"/><path d="M10 8c-2 1-2 4 0 7s5 6 8 7c2 0 3-1 3-2l-3-2-2 1c-2-1-4-3-5-5l1-2-2-4z" fill="#2b2b2b"/></svg>
      <span class="contact__name">Ray</span><span>0491 627 318</span>
    </div>
  </header>
  <div class="photo-strip">
    <div class="photo photo--plans" role="img" aria-label="Multimeter probes resting on electrical plans"></div>
    <div class="photo photo--board" role="img" aria-label="Electrician testing wiring in a switchboard"></div>
    <div class="photo photo--stripper" role="img" aria-label="Hands stripping coloured wires with pliers"></div>
    <div class="photo photo--meter" role="img" aria-label="Clamp meter testing circuit breakers"></div>
  </div>
  <div class="band">
    <svg class="chevrons" viewBox="0 0 36 34" aria-hidden="true"><path d="M2 2l14 15L2 32M18 2l14 15-14 15" fill="none" stroke="#d0282c" stroke-width="5"/></svg>
    <span class="band__title">Electrical Services</span>
    <span class="sectors"><span>residential</span><span>»</span><span>commercial</span><span>»</span><span>industrial</span></span>
  </div>
</section>

<section class="flyer flyer--back">
  <header class="head">
    <div class="brand"><span class="brand__name">Brightvolt</span><span class="brand__sub">Electrical Services</span></div>
    <div class="contact">
      <svg viewBox="0 0 30 30" aria-hidden="true"><circle cx="15" cy="15" r="13" fill="none" stroke="#2b2b2b" stroke-width="2"/><path d="M10 8c-2 1-2 4 0 7s5 6 8 7c2 0 3-1 3-2l-3-2-2 1c-2-1-4-3-5-5l1-2-2-4z" fill="#2b2b2b"/></svg>
      <span class="contact__name">Ray</span><span>0491 627 318</span>
    </div>
  </header>
  <div class="services">
    <p class="experience">Over 25 years Industry Experience</p>
    <h2 class="services__title">
      <svg class="chevrons" viewBox="0 0 36 34" aria-hidden="true"><path d="M2 2l14 15L2 32M18 2l14 15-14 15" fill="none" stroke="#d0282c" stroke-width="5"/></svg>
      Services
    </h2>
    <ul class="service-list service-list--left">
      <li>Electrical Design</li>
      <li>Installation</li>
      <li>Repairs &amp; Maintenance</li>
    </ul>
    <ul class="service-list service-list--right">
      <li>Communications Installation</li>
      <li>Cabling</li>
      <li>Maintenance &amp; Repairs</li>
    </ul>
  </div>
  <div class="band">
    <span>Service Calls</span><span>•</span><span>Quick Response Time</span><span>•</span><span>Professional Service</span>
  </div>
</section>

</body>
</html>
```